Glenmoor Slab (glenmoorslabpanels.com)

We are looking for a redesign of the entire site. We'd like to first drill down a home page design and make sure the aesthetic fits the brand, then we want to scale out the rest of the pages. The site is a basic lead generation site that focuses on selling Synthetic Ice rinks. There are two components, residential rinks, and commercial rinks. We want the primary focus to be on selling commercial rinks and the secondary to be on residential rinks.

```html
<!DOCTYPE html>
<html lang="en">
<head>
<meta charset="utf-8">
<title>Glenmoor Slab – Synthetic Ice</title>
<link href="https://fonts.googleapis.com/css2?family=Montserrat:ital,wght@0,400;0,500;0,600;0,700;1,800&display=swap" rel="stylesheet">
<style>
:root{
  --navy:#0b4e82;
  --navy-deep:#08446f;
  --red:#be1e2d;
  --ink:#111318;
  --text:#3a3d44;
  --white:#ffffff;
  --ice:#eef6fd;
  --footer:#222222;
  --footer-line:#555555;
  --star:#f5b800;
}
*{box-sizing:border-box;margin:0;padding:0}
html,body{width:1200px;height:4720px;overflow:hidden}
body{position:relative;font-family:"Montserrat",sans-serif;background:var(--white);color:var(--text)}
.abs{position:absolute}
.heading{font-family:"Montserrat",sans-serif;font-style:italic;font-weight:800;text-transform:uppercase;color:var(--ink);letter-spacing:.5px}
.copy{font-size:12.5px;line-height:28.5px;text-transform:uppercase;font-weight:500}
.btn{display:flex;align-items:center;justify-content:center;font-size:12.5px;font-weight:700;text-transform:uppercase;letter-spacing:.5px;clip-path:polygon(6% 0,100% 0,94% 100%,0 100%)}
.btn-blue{background:linear-gradient(90deg,#2d6ea4,var(--navy-deep));color:var(--white)}
.btn-white{background:var(--white);color:var(--ink)}
.photo{border-radius:0}

/* header */
.site-header{left:0;top:0;width:1200px;height:82px;border-bottom:1px solid #e6e6e6}
.brand{left:100px;top:24px;display:flex;align-items:center;gap:10px;font-weight:700;font-size:24px;color:var(--navy);text-transform:uppercase;letter-spacing:1px}
.brand-mark{width:14px;height:14px;background:var(--red)}
.nav{left:405px;top:32px;display:flex;gap:38px;font-size:11.5px;text-transform:uppercase;color:#555}
.nav .active{color:var(--ink);font-weight:700}
.nav-cta{left:932px;top:21px;width:168px;height:42px;background:linear-gradient(90deg,#d6363f,var(--red));color:var(--white)}

/* hero */
.hero-title{left:0;top:205px;width:1200px;text-align:center;font-size:50px;line-height:52px}
.hero-copy{left:190px;top:332px;width:820px;text-align:center;font-size:12.5px;line-height:24.5px}
.hero-btn{left:522px;top:448px;width:168px;height:42px}
.slide{left:190px;top:533px;width:820px;height:353px;background:linear-gradient(180deg,#1b2332 0%,#3a4456 45%,#9fb0c2 75%,#d7e0ea 100%)}
.arrow{width:42px;height:42px;border-radius:50%;display:flex;align-items:center;justify-content:center}

/* sections */
.band-blue{left:0;top:987px;width:1200px;height:605px;background:var(--navy)}
.band-red{left:0;top:2238px;width:1200px;height:647px;background:var(--red)}
.band-ice{left:0;top:3530px;width:1200px;height:692px;background:var(--ice)}
.on-dark{color:var(--white)}
.sec-title{font-size:40px;line-height:46px}

/* checks */
.check-item{display:flex;gap:24px;align-items:center;width:540px}
.check-dot{flex:0 0 34px;height:34px;border-radius:50%;background:var(--white);box-shadow:0 2px 8px rgba(0,0,0,.12);display:flex;align-items:center;justify-content:center}

/* testimonials */
.card{background:var(--white);text-align:center}
.card-head{display:flex;align-items:center;gap:16px;justify-content:center}
.avatar{border-radius:50%;background:linear-gradient(180deg,#c9ced6,#5a6472);position:relative}
.quote{position:absolute;right:-16px;bottom:-6px;font-family:Georgia,serif;font-weight:700;color:var(--ink);line-height:1}
.name{font-style:italic;font-weight:800;text-transform:uppercase;color:var(--ink);text-align:left}
.role{font-style:italic;text-transform:uppercase;color:#aaa;text-align:left}
.stars{color:var(--star)}
.dots{left:556px;top:4112px;display:flex;gap:12px}
.dots span{width:12px;height:12px;border-radius:50%;background:#cfd9e3}
.dots span.on{background:var(--navy)}

/* footer */
.site-footer{left:0;top:4222px;width:1200px;height:498px;background:var(--footer);color:var(--white)}
.f-brand{left:125px;top:4352px;display:flex;align-items:center;gap:10px;font-weight:700;font-size:24px;text-transform:uppercase;letter-spacing:1px;color:var(--white)}
.f-text{left:125px;top:4410px;width:330px;font-size:12.5px;line-height:28px;text-transform:uppercase}
.f-rule{width:1px;height:210px;background:var(--footer-line);top:4375px}
.f-title{font-size:15px;font-weight:700;text-transform:uppercase;letter-spacing:.5px}
.f-links{left:520px;top:4370px;width:200px;text-align:center}
.f-links li{list-style:none;font-size:12px;text-transform:uppercase;line-height:33px}
.f-contact{left:800px;top:4370px}
.f-row{display:flex;align-items:center;gap:20px;font-size:11px;text-transform:uppercase;margin-top:22px}
.f-ico{width:40px;height:40px;border-radius:50%;background:var(--red);display:flex;align-items:center;justify-content:center}
.copyright{left:0;top:4680px;width:1200px;height:40px;border-top:1px solid #3a3a3a;text-align:center;font-size:12px;line-height:40px;text-transform:uppercase;color:var(--white)}
.copyright b{font-weight:700}
</style>
</head>
<body>

<header class="abs site-header">
  <div class="abs brand"><span class="brand-mark"></span>Glenmoor Slab</div>
  <nav class="abs nav">
    <span class="active">Home</span><span>About Us</span><span>Residential Rinks</span><span>Commercial Rinks</span>
  </nav>
  <a class="abs btn nav-cta">Contact Us</a>
</header>

<section>
  <h1 class="abs heading hero-title">The Ultimate Synthetic<br>Ice Experience</h1>
  <p class="abs hero-copy">Lorem Ipsum is simply dummy text of the printing and typesetting industry. Lorem Ipsum has been the industry's standard dummy text ever since the 1500s, when an unknown printer took a galley of type and scrambled it to make a type specimen book.</p>
  <a class="abs btn btn-blue hero-btn">Shop Now</a>
  <div class="abs slide" role="img" aria-label="Floodlit indoor arena with an ice rink and packed stands"></div>
  <div class="abs arrow" style="left:124px;top:688px;background:var(--red)">
    <svg width="14" height="14" viewBox="0 0 14 14"><path d="M9 2 4 7l5 5" fill="none" stroke="#fff" stroke-width="2"/></svg>
  </div>
  <div class="abs arrow" style="left:1032px;top:688px;background:var(--navy)">
    <svg width="14" height="14" viewBox="0 0 14 14"><path d="M5 2l5 5-5 5" fill="none" stroke="#fff" stroke-width="2"/></svg>
  </div>
</section>

<section>
  <div class="abs band-blue"></div>
  <h2 class="abs heading sec-title on-dark" style="left:125px;top:1093px">About Us</h2>
  <p class="abs copy on-dark" style="left:125px;top:1162px;width:490px">Lorem Ipsum is simply dummy text of the printing and typesetting industry. Lorem Ipsum has been the industry's standard dummy text ever since the 1500s, when an unknown printer took a galley of type and scrambled it to make a type specimen book. It has survived not only five centuries, but also the leap into electronic typesetting, remaining essentially unchanged.</p>
  <a class="abs btn btn-white" style="left:125px;top:1402px;width:168px;height:42px">Read More</a>
  <div class="abs photo" style="left:657px;top:1045px;width:418px;height:447px;background:linear-gradient(180deg,#7a5a3c 0%,#b58a5a 25%,#4e5560 55%,#7d8a92 100%)" role="img" aria-label="Two girls skating together on a rink"></div>
</section>

<section>
  <div class="abs photo" style="left:125px;top:1692px;width:418px;height:446px;background:linear-gradient(180deg,#6d7480 0%,#a5acb4 35%,#e3e5e8 55%,#d8dadd 100%)" role="img" aria-label="Hockey goal on a backyard synthetic rink"></div>
  <h2 class="abs heading sec-title" style="left:588px;top:1740px">Residential Rinks</h2>
  <p class="abs copy" style="left:588px;top:1810px;width:490px">Lorem Ipsum is simply dummy text of the printing and typesetting industry. Lorem Ipsum has been the industry's standard dummy text ever since the 1500s, when an unknown printer took a galley of type and scrambled it to make a type specimen book. It has survived not only five centuries, but also the leap into electronic typesetting, remaining essentially unchanged.</p>
  <a class="abs btn btn-blue" style="left:588px;top:2050px;width:168px;height:42px">Learn More</a>
</section>

<section>
  <div class="abs band-red"></div>
  <h2 class="abs heading sec-title on-dark" style="left:125px;top:2386px">Commercial Rinks</h2>
  <p class="abs copy on-dark" style="left:125px;top:2455px;width:490px">Lorem Ipsum is simply dummy text of the printing and typesetting industry. Lorem Ipsum has been the industry's standard dummy text ever since the 1500s, when an unknown printer took a galley of type and scrambled it to make a type specimen book. It has survived not only five centuries, but also the leap into electronic typesetting, remaining essentially unchanged.</p>
  <a class="abs btn btn-white" style="left:125px;top:2695px;width:168px;height:42px">Learn More</a>
  <div class="abs photo" style="left:657px;top:2338px;width:418px;height:445px;background:linear-gradient(180deg,#5b6470 0%,#8a5a5e 35%,#c9d3dc 55%,#e6ecf1 100%)" role="img" aria-label="Large indoor arena rink with skaters"></div>
</section>

<section>
  <div class="abs photo" style="left:125px;top:2985px;width:418px;height:445px;background:linear-gradient(180deg,#5b6470 0%,#8a5a5e 35%,#c9d3dc 55%,#e6ecf1 100%)" role="img" aria-label="Skaters on a commercial indoor rink"></div>
  <h2 class="abs heading sec-title" style="left:594px;top:3038px">Why Choose Us</h2>
  <div class="abs" style="left:594px;top:3104px;display:flex;flex-direction:column;gap:9px">
    <div class="check-item"><span class="check-dot"><svg width="16" height="16" viewBox="0 0 16 16"><path d="M3 8.5l3.2 3L13 4.5" fill="none" stroke="#0b4e82" stroke-width="2.4"/></svg></span><p class="copy">Lorem Ipsum is simply dummy text of the printing and typesetting industry. Lorem Ipsum has been the industry's standard dummy text ever since the 1500s.</p></div>
    <div class="check-item"><span class="check-dot"><svg width="16" height="16" viewBox="0 0 16 16"><path d="M3 8.5l3.2 3L13 4.5" fill="none" stroke="#0b4e82" stroke-width="2.4"/></svg></span><p class="copy">Lorem Ipsum is simply dummy text of the printing and typesetting industry. Lorem Ipsum has been the industry's standard dummy text ever since the 1500s.</p></div>
    <div class="check-item"><span class="check-dot"><svg width="16" height="16" viewBox="0 0 16 16"><path d="M3 8.5l3.2 3L13 4.5" fill="none" stroke="#0b4e82" stroke-width="2.4"/></svg></span><p class="copy">Lorem Ipsum is simply dummy text of the printing and typesetting industry. Lorem Ipsum has been the industry's standard dummy text ever since the 1500s.</p></div>
  </div>
</section>

<section>
  <div class="abs band-ice"></div>
  <h2 class="abs heading sec-title" style="left:0;top:3628px;width:1200px;text-align:center">Testimonials</h2>

  <article class="abs card" style="left:113px;top:3776px;width:265px;height:244px;padding:24px 20px">
    <div class="card-head"><div class="avatar" style="width:56px;height:56px" role="img" aria-label="Customer portrait"><span class="quote" style="font-size:34px">&#8220;</span></div>
      <div><div class="name" style="font-size:14px">Dana Whitfield</div><div class="role" style="font-size:9px">Small Business Owner</div></div></div>
    <p style="font-size:9px;line-height:20px;text-transform:uppercase;margin-top:20px">Our rink was ready in days and the kids skate every evening. Great panels, fast delivery and friendly support.</p>
    <div class="stars" style="font-size:10px;margin-top:8px">★★★★★</div>
  </article>

  <article class="abs card" style="left:411px;top:3722px;width:378px;height:346px;padding:30px 30px">
    <div class="card-head"><div class="avatar" style="width:82px;height:82px" role="img" aria-label="Customer portrait"><span class="quote" style="font-size:50px">&#8220;</span></div>
      <div style="margin-left:14px"><div class="name" style="font-size:20px">Dana Whitfield</div><div class="role" style="font-size:12px">Small Business Owner</div></div></div>
    <p style="font-size:13px;line-height:28.5px;text-transform:uppercase;margin-top:34px">Lorem Ipsum is simply dummy text of the printing and typesetting industry. Lorem Ipsum has been the industry's standard dummy text ever</p>
    <div class="stars" style="font-size:14px;margin-top:12px">★★★★★</div>
  </article>

  <article class="abs card" style="left:821px;top:3776px;width:265px;height:244px;padding:24px 20px">
    <div class="card-head"><div class="avatar" style="width:56px;height:56px" role="img" aria-label="Customer portrait"><span class="quote" style="font-size:34px">&#8220;</span></div>
      <div><div class="name" style="font-size:14px">Dana Whitfield</div><div class="role" style="font-size:9px">Small Business Owner</div></div></div>
    <p style="font-size:9px;line-height:20px;text-transform:uppercase;margin-top:20px">Lorem Ipsum is simply dummy text of the printing and typesetting industry. Lorem Ipsum has been the industry's standard dummy text ever</p>
    <div class="stars" style="font-size:10px;margin-top:8px">★★★★★</div>
  </article>

  <div class="abs dots"><span class="on"></span><span></span><span></span><span></span></div>
</section>

<footer>
  <div class="abs site-footer"></div>
  <div class="abs f-brand"><span class="brand-mark"></span>Glenmoor Slab</div>
  <p class="abs f-text on-dark">Lorem Ipsum is simply dummy text of the printing and typesetting industry. Lorem Ipsum has been the industry's standard dummy text ever since the 1500s, when an unknown printer took.</p>
  <div class="abs f-rule" style="left:493px"></div>
  <div class="abs f-rule" style="left:747px"></div>
  <div class="abs f-links on-dark">
    <div class="f-title" style="margin-bottom:14px">Quick Links</div>
    <ul><li>Home</li><li>About Us</li><li>Residential Links</li><li>Commercial Links</li><li>Contact Us</li></ul>
  </div>
  <div class="abs f-contact on-dark">
    <div class="f-title">Contact Info</div>
    <div class="f-row"><span class="f-ico"><svg width="18" height="18" viewBox="0 0 18 18"><path d="M9 16s-5-5-5-9a5 5 0 0 1 10 0c0 4-5 9-5 9z" fill="none" stroke="#fff" stroke-width="1.5"/><circle cx="9" cy="7" r="1.8" fill="none" stroke="#fff" stroke-width="1.5"/></svg></span>Lorem Ipsum is simple dummy text</div>
    <div class="f-row"><span class="f-ico"><svg width="18" height="18" viewBox="0 0 18 18"><path d="M4 2.5l3 .5 1 3-1.8 1.4a9 9 0 0 0 4.4 4.4L12 10l3 1 .5 3c-1 1-2.5 1.5-4 1A13 13 0 0 1 3 6.5c-.5-1.5 0-3 1-4z" fill="none" stroke="#fff" stroke-width="1.4"/></svg></span>Call us on : 021 4470 1182</div>
    <div class="f-row"><span class="f-ico"><svg width="18" height="18" viewBox="0 0 18 18"><rect x="2.5" y="4" width="13" height="10" fill="none" stroke="#fff" stroke-width="1.4"/><path d="M2.5 4.5 9 10l6.5-5.5" fill="none" stroke="#fff" stroke-width="1.4"/></svg></span>info@glenmoorslabpanels.com</div>
  </div>
  <div class="abs copyright">Copyright © 2023 <b>Glenmoor Slab</b>. All rights reserved.</div>
</footer>

</body>
</html>
```